TV - business card

Tidewell Vantage is an insurance brokerage firm, inovative, proactive, vigorous, which aims to become the leader of the insurance brokers in Anfrica. We should like to get some designs which should be avoided also in Gray / Metallic for the Administration and Orange / Blue for the Managers (ike in the picture sent). The Blue / Green logo is not the correct one, but the source of the file. Please adjust the color accordingly for the business cards. 1 / Orange / Blue 2 / Gray / Metallic We want something classic but which is transmitted strenght, inovation, modernity and most of all, rapidity. We want something start-up like, very punchy and catching eye remaining profesional at the same time. Name: Delton Ashgrove Fenwright: Managing Director Address: N ° 73/74 Cmt. Bolembe - R / C 2B Esquerda - Bairro Quimbuta - Luanda Tel: (+244) 947 385 619 Email: delton.ashgrove@tidewell-v.com Website: www.tidewell-v. com We want classic in the front and creative, colorfull at the back. The cards will be printed in relief, with very high quality of paper.
Industry/Entity Type
Insurance Broker
Colors
Designer to choose colors to be used in the design.
Look and feel

```html
<!DOCTYPE html>
<html lang="en">
<head>
<meta charset="utf-8">
<title>Tidewell Vantage – Business Card</title>
<link rel="stylesheet" href="https://fonts.googleapis.com/css2?family=Open+Sans:wght@400;700&family=Cinzel:wght@400&display=swap">
<style>
  :root{
    --navy:#22346c;
    --orange:#f15a24;
    --orange-mid:#f7901e;
    --amber:#fbb03b;
    --white:#ffffff;
    --stage:#ececec;
  }
  *{margin:0;padding:0;box-sizing:border-box}
  html,body{width:1200px;height:1200px;overflow:hidden}
  body{background:var(--stage);position:relative;font-family:"Open Sans",sans-serif}

  .card{position:absolute;width:474px;height:269px;overflow:hidden}
  .card--front{left:355px;top:154px;background:var(--navy)}
  .card--back{left:356px;top:747px;background:linear-gradient(90deg,var(--orange) 0%,var(--orange-mid) 50%,var(--orange) 100%)}

  .band{position:absolute;display:flex;align-items:center}
  .band--name{left:0;top:71px;width:201px;height:26px;background:var(--orange);padding-left:11px;
    color:var(--white);font-weight:700;font-size:11px;letter-spacing:.1px;white-space:nowrap}
  .band--role{left:357px;top:181px;width:117px;height:25px;background:var(--orange);justify-content:flex-end;padding-right:6px;
    color:var(--white);font-size:10px;white-space:nowrap}

  .emblem{position:absolute;display:flex;align-items:center;justify-content:center;text-align:center;border-radius:50%;
    color:var(--white);font-weight:700;font-size:15px;line-height:1.2;letter-spacing:.5px}
  .emblem--front{left:204px;top:40px;width:188px;height:188px;border:12px solid var(--orange-mid)}
  .emblem--back{left:192px;top:39px;width:190px;height:190px;background:var(--navy)}

  .brand-dot{position:absolute;left:69px;top:19px;width:50px;height:50px;border-radius:50%;border:4px solid var(--white)}
  .band--brand{left:0;top:75px;width:200px;height:16px;background:var(--white);padding-left:22px;
    color:var(--navy);font-weight:700;font-size:11px;white-space:nowrap}
  .band--accent{left:363px;top:184px;width:111px;height:15px;background:var(--white)}

  .contact{position:absolute;left:24px;top:176px;list-style:none;font-family:"Cinzel",serif;color:var(--white);font-size:9.5px}
  .contact li{display:flex;align-items:center;gap:5px;height:21px;white-space:nowrap}
  .contact svg{width:12px;height:12px;flex:none;fill:var(--white)}
</style>
</head>
<body>

<section class="card card--front" aria-label="Card front">
  <div class="band band--name">DELTON ASHGROVE FENWRIGHT</div>
  <div class="emblem emblem--front">Tidewell<br>Vantage</div>
  <div class="band band--role">Managing Director</div>
</section>

<section class="card card--back" aria-label="Card back">
  <div class="brand-dot"></div>
  <div class="band band--brand">TIDEWELL-VANTAGE</div>
  <div class="emblem emblem--back">Tidewell<br>Vantage</div>
  <div class="band band--accent"></div>
  <ul class="contact">
    <li><svg viewBox="0 0 24 24"><path d="M6.6 10.8a15 15 0 0 0 6.6 6.6l2.2-2.2a1 1 0 0 1 1-.25 11.4 11.4 0 0 0 3.6.57 1 1 0 0 1 1 1V20a1 1 0 0 1-1 1A17 17 0 0 1 3 4a1 1 0 0 1 1-1h3.5a1 1 0 0 1 1 1c0 1.25.2 2.45.57 3.57a1 1 0 0 1-.25 1z"/></svg>(+244) 947 385 619</li>
    <li><svg viewBox="0 0 24 24"><path d="M12 2a10 10 0 1 0 0 20 10 10 0 0 0 0-20zm6.9 6h-2.9a15 15 0 0 0-1.4-3.6A8 8 0 0 1 18.9 8zM12 4c.8 1.2 1.5 2.5 1.9 4h-3.8c.4-1.5 1.1-2.8 1.9-4zM4.3 14a8 8 0 0 1 0-4h3.4a16 16 0 0 0 0 4zm.8 2h2.9c.3 1.3.8 2.5 1.4 3.6A8 8 0 0 1 5.1 16zM8 8H5.1a8 8 0 0 1 4.3-3.6C8.8 5.5 8.4 6.7 8 8zm4 12c-.8-1.2-1.5-2.5-1.9-4h3.8c-.4 1.5-1.1 2.8-1.9 4zm2.3-6H9.7a14 14 0 0 1 0-4h4.6a14 14 0 0 1 0 4zm.3 5.6c.6-1.1 1.1-2.3 1.4-3.6h2.9a8 8 0 0 1-4.3 3.6zm1.7-5.6a16 16 0 0 0 0-4h3.4a8 8 0 0 1 0 4z"/></svg>www.tidewell-v. com</li>
    <li><svg viewBox="0 0 24 24"><path d="M2 5h20v14H2zm2 2v.5l8 5 8-5V7zm0 2.8V17h16V9.8l-8 5z"/></svg>delton.ashgrove@tidewell-v.com</li>
    <li><svg viewBox="0 0 24 24"><path d="M12 2a7 7 0 0 0-7 7c0 5 7 13 7 13s7-8 7-13a7 7 0 0 0-7-7zm0 9.5A2.5 2.5 0 1 1 12 6.5a2.5 2.5 0 0 1 0 5z"/></svg>N ° 73/74 Cmt. Bolembe - R / C 2B Esquerda - Bairro Quimbuta - Luanda</li>
  </ul>
</section>

</body>
</html>
```